Author Needs a Book Cover for a Business Book

Title: THE AMBER HARBOR LANTERN LEDGER
Subtitle: Rivers, Orchards, and Weathervanes
Author: Belvina Throckett-Ashe, MBA, EdM, ACC, CPTD

Context: Please design a business-oriented book cover, with a minimalist, clean, and professional look.

Image to include a person (the coach either as a woman or non-specific) gender) looking into the horizon and see the three types of coaching engagement which are: group, 1:1 or virtual

Images need to be high definition for a book cover (print, digital, and audio). Back and spine design, jacket cover, audiobook cover and source files.
Format: Vector (but unsure)
AI assisted is ok, but would prefer original images
Note: I've attached a PPT with inspirational ideas but I am open to ideas.

```html
<!DOCTYPE html>
<html lang="en">
<head>
<meta charset="utf-8">
<title>The Amber Harbor Lantern Ledger — Book Cover</title>
<link rel="stylesheet" href="https://fonts.googleapis.com/css2?family=Bebas+Neue&family=Lexend:wght@500;600&display=swap">
<style>
  :root {
    --navy: #263e7d;
    --navy-deep: #22366e;
    --cyan: #00b5dc;
    --white: #ffffff;
    --backdrop: #4f4f4f;
  }
  * { margin: 0; padding: 0; box-sizing: border-box; }
  html, body {
    width: 1200px;
    height: 1200px;
    overflow: hidden;
    background: var(--backdrop);
  }
  .canvas {
    width: 1200px;
    height: 1200px;
    display: flex;
    align-items: center;
    justify-content: center;
  }
  .book-cover {
    width: 805px;
    height: 1140px;
    display: block;
  }
  .gradient-top { stop-color: var(--navy-deep); }
  .gradient-mid { stop-color: var(--navy); }
  .gradient-end { stop-color: var(--cyan); }
  .title-disc { fill: var(--white); }
  .title {
    font-family: "Bebas Neue", "Oswald", sans-serif;
  }
  .title-line--lead { fill: var(--cyan); font-size: 84px; }
  .title-line--middle { fill: var(--navy); font-size: 121px; }
  .title-line--last { fill: var(--cyan); font-size: 121px; }
  .subtitle {
    font-family: "Bebas Neue", "Oswald", sans-serif;
    font-size: 38px;
    fill: var(--navy);
  }
  .author-name {
    font-family: "Lexend", "Montserrat", sans-serif;
    font-weight: 600;
    font-size: 28px;
    fill: var(--cyan);
    text-anchor: middle;
  }
  .author-credentials {
    font-family: "Lexend", "Montserrat", sans-serif;
    font-weight: 600;
    font-size: 16px;
    fill: var(--cyan);
    text-anchor: middle;
  }
</style>
</head>
<body>
<main class="canvas">
  <svg class="book-cover" viewBox="0 0 840 1190" xmlns="http://www.w3.org/2000/svg" aria-label="Book cover: The Amber Harbor Lantern Ledger by Belvina Throckett-Ashe">
    <defs>
      <linearGradient id="cover-backdrop-gradient" x1="0" y1="0" x2="0.35" y2="1">
        <stop class="gradient-top" offset="0"/>
        <stop class="gradient-mid" offset="0.6"/>
        <stop class="gradient-end" offset="1"/>
      </linearGradient>
    </defs>

    <rect class="cover-artwork" x="0" y="0" width="840" height="1190" fill="url(#cover-backdrop-gradient)" role="img" aria-label="Decorative backdrop area in navy and cyan tones"/>

    <circle class="title-disc" cx="420" cy="595" r="365"/>

    <g class="title">
      <text class="title-line--lead" x="153" y="495" textLength="532" lengthAdjust="spacing">THE AMBER HARBOR</text>
      <text class="title-line--middle" x="153" y="597" textLength="532" lengthAdjust="spacing">LANTERN</text>
      <text class="title-line--last" x="153" y="703" textLength="532" lengthAdjust="spacing">LEDGER</text>
    </g>
    <text class="subtitle" x="155" y="750" textLength="535" lengthAdjust="spacing">RIVERS, ORCHARDS, AND WEATHERVANES</text>

    <text class="author-name" x="423" y="799">Belvina Throckett-Ashe</text>
    <text class="author-credentials" x="423" y="830">MBA, EdM, ACC, CPTD</text>
  </svg>
</main>
</body>
</html>
```